Simple+Professional tech feel + warm and friendly box design for pet test kit

Project Name: 10-Minute Canine & Feline Rapid Test Kit Packaging Design
Target Brand Reference: VETRALUX (South Korea) styles
Design Style Direction: Professional tech feel + warm and friendly
Professionalism (Professional): Clear typography and distinct information hierarchy to reflect the product’s scientific rigor and accuracy.
Technological: Reflected through clean graphics and a minimalist layout.
Friendly: Utilise soft, warm colour combinations to convey care for pets and well-wishes for their health.
International: The design should align with mainstream aesthetics and avoid cultural ambiguities.

Target Market(s)
European Union and the United States
Industry/Entity Type
Veterinary Medical
Look and feel
Each slider illustrates characteristics of the customer's brand and the style your logo design should communicate.

```html
<!DOCTYPE html>
<html lang="en">
<head>
<meta charset="UTF-8">
<title>10-Minute Canine &amp; Feline Rapid Test Kit – Packaging</title>
<link href="https://fonts.googleapis.com/css2?family=Lexend:wght@300;400;500;700&family=Zilla+Slab:wght@300&family=Nunito+Sans:wght@400;700&display=swap" rel="stylesheet">
<style>
  :root {
    --page: #dcd8d2;
    --panel: #eeeff1;
    --panel-side: #e4e5e8;
    --blue: #2c5f9e;
    --teal: #2a9a86;
    --teal-text: #3aa892;
    --ink: #3b3b3b;
    --white: #ffffff;
  }
  * { box-sizing: border-box; margin: 0; padding: 0; }
  html, body { width: 1200px; height: 900px; overflow: hidden; }
  body {
    background: var(--page);
    position: relative;
    font-family: "Lexend", sans-serif;
  }
  .box-net {
    position: absolute;
    left: 100px;
    top: 150px;
    width: 1000px;
    height: 600px;
    display: flex;
    box-shadow: 0 18px 40px rgba(0,0,0,0.12);
  }

  /* Side panel */
  .side-panel {
    position: relative;
    width: 200px;
    height: 600px;
    background: var(--panel-side);
    border-right: 1px solid #d2d4d8;
  }
  .side-panel .band-top {
    position: absolute; left: 0; top: 50px; width: 100%; height: 45px;
    background: var(--blue);
  }
  .side-panel .band-bottom {
    position: absolute; left: 0; bottom: 0; width: 100%; height: 62px;
    background: var(--teal);
  }
  .side-info {
    position: absolute; left: 0; top: 170px; width: 100%;
    text-align: center;
    font-family: "Nunito Sans", sans-serif;
    font-size: 12.5px; line-height: 1.55;
    color: var(--ink);
  }
  .side-info strong { font-weight: 700; }
  .side-note {
    position: absolute; left: 18px; right: 18px; top: 385px;
    text-align: center;
    font-family: "Nunito Sans", sans-serif;
    font-size: 9.5px; line-height: 1.4;
    color: var(--ink);
  }
  .storage-icons {
    position: absolute; left: 16px; top: 455px;
    width: 168px; height: 40px;
  }

  /* Front panel */
  .front-panel {
    position: relative;
    width: 800px;
    height: 600px;
    background: var(--panel);
  }
  .front-panel .band-top {
    position: absolute; left: 0; top: 50px; width: 640px; height: 45px;
    background: var(--blue);
    display: flex; align-items: center; padding-left: 34px;
  }
  .front-panel .band-top-end {
    position: absolute; right: 0; top: 50px; width: 60px; height: 45px;
    background: var(--blue);
  }
  .brand-name {
    color: var(--white);
    font-family: "Lexend", sans-serif;
    font-weight: 500;
    font-size: 25px;
    letter-spacing: 0.3px;
  }
  .test-count {
    position: absolute; left: 640px; top: 34px; width: 100px;
    text-align: center; color: var(--teal-text);
  }
  .test-count .number {
    display: block; font-weight: 700; font-size: 62px; line-height: 1;
  }
  .test-count .unit {
    display: block; font-weight: 400; font-size: 14px; margin-top: 10px;
  }
  .product-title {
    position: absolute; left: 0; top: 190px; width: 100%;
    text-align: center;
    font-weight: 700; font-size: 40px;
    color: var(--blue);
    letter-spacing: 0.2px;
  }
  .heart-art {
    position: absolute; left: 48px; top: 252px; width: 160px; height: 150px;
    border-radius: 50% 50% 45% 45%;
    background: radial-gradient(circle at 50% 45%, rgba(58,168,146,0.25), rgba(58,168,146,0.08));
  }
  .product-subtitle {
    position: absolute; left: 218px; top: 262px;
    font-weight: 300; font-size: 34px;
    color: var(--teal-text);
  }
  .approval-seal {
    position: absolute; left: 600px; top: 300px;
    width: 110px; height: 54px;
    transform: rotate(-12deg);
  }
  .audience-line {
    position: absolute; left: 150px; top: 440px;
    font-family: "Zilla Slab", serif;
    font-weight: 300; font-size: 38px;
    color: var(--teal-text);
    transform: rotate(-2deg);
  }
  .dog-art {
    position: absolute; left: 12px; top: 420px; width: 120px; height: 140px;
    border-radius: 40% 40% 10% 10%;
    background: linear-gradient(180deg, rgba(58,168,146,0.18), rgba(58,168,146,0.06));
  }
  .cat-art {
    position: absolute; left: 610px; top: 372px; width: 86px; height: 118px;
    border-radius: 40% 40% 10% 10%;
    background: linear-gradient(180deg, rgba(58,168,146,0.18), rgba(58,168,146,0.06));
  }
  .front-panel .band-bottom {
    position: absolute; left: 0; bottom: 0; width: 100%; height: 62px;
    background: var(--teal);
  }
  .maker-name {
    position: absolute; right: 36px; bottom: 76px;
    font-weight: 500; font-size: 17px;
    color: var(--teal-text);
  }
</style>
</head>
<body>
  <div class="box-net">
    <section class="side-panel">
      <div class="band-top"></div>
      <div class="side-info">
        <p>A Clear View into Pet Health</p>
        <p>Made by Morvane</p>
        <p><strong>Morvane Biotech Limited</strong></p>
        <p>Web:www.morvane-bio.com</p>
        <p>E-mail:sales@morvane-bio.com</p>
      </div>
      <p class="side-note">(For accurate results, please read the instructions carefully before use)</p>
      <svg class="storage-icons" viewBox="0 0 168 40" aria-label="Storage and usage symbols">
        <g fill="none" stroke="#333" stroke-width="1.6">
          <circle cx="14" cy="20" r="11"/>
          <line x1="6" y1="12" x2="22" y2="28"/>
          <path d="M36 18 a10 8 0 0 1 20 0 z"/>
          <path d="M46 18 v12 a3 3 0 0 1 -6 0"/>
          <circle cx="74" cy="18" r="4"/>
          <g>
            <line x1="74" y1="8" x2="74" y2="11"/><line x1="74" y1="25" x2="74" y2="28"/>
            <line x1="64" y1="18" x2="67" y2="18"/><line x1="81" y1="18" x2="84" y2="18"/>
          </g>
          <path d="M96 28 l6 -18 M102 10 v18"/>
          <line x1="99" y1="12" x2="108" y2="12"/>
          <line x1="94" y1="28" x2="102" y2="28"/>
          <rect x="124" y="6" width="38" height="28"/>
        </g>
        <text x="143" y="25" text-anchor="middle" font-family="Nunito Sans, sans-serif" font-weight="700" font-size="12" fill="#333">IVD</text>
      </svg>
      <div class="band-bottom"></div>
    </section>

    <section class="front-panel">
      <div class="band-top"><span class="brand-name">ClarVet™</span></div>
      <div class="band-top-end"></div>
      <div class="test-count"><span class="number">5</span><span class="unit">Tests/Kit</span></div>

      <h1 class="product-title">10-Minute Canine &amp; Feline</h1>
      <div class="heart-art" role="img" aria-label="Heart outline with two paw prints"></div>
      <p class="product-subtitle">Rapid Test Kit</p>

      <svg class="approval-seal" viewBox="0 0 110 54" aria-hidden="true">
        <rect x="2" y="2" width="106" height="50" rx="22" fill="none" stroke="#4a6fae" stroke-width="2.5"/>
        <rect x="8" y="8" width="94" height="38" rx="17" fill="none" stroke="#4a6fae" stroke-width="1.2"/>
      </svg>

      <div class="dog-art" role="img" aria-label="Line illustration of a sitting dog"></div>
      <p class="audience-line">For Dogs and Cats</p>
      <div class="cat-art" role="img" aria-label="Line illustration of a sitting cat"></div>

      <span class="maker-name">Morvane</span>
      <div class="band-bottom"></div>
    </section>
  </div>
</body>
</html>
```